St Louis Electrician Needing a Business Card Design!!

We are a St Louis based electrical contracting firm that needs help designing a business card. We have a logo and I have another image that I would like to incorporate. Open to ideas..Thanks!!

Industry/Entity Type

Business

Requirements
Must have
• there are two downloads...one is the logo and the other is what i was wanting coming off the logo...the light rays. Like the logo with the blue background...Was thinking the whole card would be that color blue.
Should not have
• No lightning bolts

```html
<!DOCTYPE html>
<html lang="en">
<head>
<meta charset="UTF-8">
<title>VoltaLine Inc. – Business Card</title>
<link rel="stylesheet" href="https://fonts.googleapis.com/css2?family=Marcellus&display=swap">
<style>
  :root {
    --backdrop: #c3ccc7;
    --card: #ffffff;
    --brand-blue: #0a40ff;
    --band-grey: #a9a9a9;
    --rule-grey: #8f8f8f;
    --name-grey: #a6a6a6;
    --ink: #1f1f1f;
  }
  html, body {
    margin: 0;
    width: 1200px;
    height: 1000px;
    overflow: hidden;
    background: var(--backdrop);
  }
  .canvas {
    position: relative;
    width: 1200px;
    height: 1000px;
  }
  .card {
    position: absolute;
    left: 360px;
    top: 60px;
    width: 480px;
    height: 880px;
    background: var(--card);
    box-shadow: 0 10px 30px rgba(0,0,0,0.18);
    overflow: hidden;
    font-family: "Marcellus", serif;
  }
  .card-shapes {
    position: absolute;
    inset: 0;
  }
  .holder {
    position: absolute;
    top: 88px;
    left: 0;
    width: 100%;
    text-align: center;
    color: var(--name-grey);
  }
  .holder-name {
    margin: 0;
    font-size: 34px;
    font-weight: 400;
    letter-spacing: 1px;
  }
  .holder-title {
    margin: 6px 0 0;
    font-size: 19px;
  }
  .company {
    position: absolute;
    top: 340px;
    left: 0;
    width: 100%;
    display: flex;
    align-items: center;
    justify-content: center;
    gap: 14px;
  }
  .company-mark {
    width: 16px;
    height: 16px;
    border-radius: 50%;
    background: var(--brand-blue);
  }
  .company-name {
    font-size: 40px;
    color: var(--brand-blue);
  }
  .contact-text {
    position: absolute;
    left: 92px;
    margin: 0;
    font-size: 18px;
    line-height: 28px;
    color: var(--ink);
  }
  .contact-phones { top: 548px; }
  .contact-web { top: 628px; }
  .contact-address { top: 708px; }
</style>
</head>
<body>
<main class="canvas">
  <article class="card">
    <svg class="card-shapes" width="480" height="880" viewBox="0 0 480 880" aria-hidden="true">
      <polygon class="top-band" points="0,0 480,0 480,120 300,232 0,200" fill="var(--brand-blue)"/>
      <polygon class="bottom-band" points="0,845 250,782 480,782 480,880 0,880" fill="var(--band-grey)"/>

      <g class="contact-rules" stroke="var(--rule-grey)" stroke-width="2">
        <line x1="90" y1="540" x2="385" y2="540"/>
        <line x1="90" y1="620" x2="385" y2="620"/>
        <line x1="90" y1="700" x2="385" y2="700"/>
      </g>

      <g class="icon-phone">
        <rect x="385" y="490" width="58" height="58" fill="var(--brand-blue)"/>
        <path d="M399 512 q15 -9 30 0 l-3 6 l-7 -2 v-3 h-10 v3 l-7 2 z" fill="#fff"/>
        <rect x="402" y="520" width="24" height="14" rx="2" fill="#fff"/>
        <circle cx="414" cy="527" r="3.5" fill="var(--brand-blue)"/>
      </g>

      <g class="icon-monitor">
        <rect x="385" y="570" width="58" height="58" fill="var(--brand-blue)"/>
        <rect x="400" y="584" width="28" height="20" fill="none" stroke="#fff" stroke-width="3"/>
        <rect x="411" y="605" width="6" height="5" fill="#fff"/>
        <rect x="404" y="610" width="20" height="3" fill="#fff"/>
      </g>

      <g class="icon-home">
        <rect x="385" y="650" width="58" height="58" fill="var(--brand-blue)"/>
        <polygon points="414,664 398,679 402,679 414,668 426,679 430,679" fill="#fff"/>
        <polygon points="403,680 414,670 425,680 425,694 417,694 417,686 411,686 411,694 403,694" fill="#fff"/>
      </g>
    </svg>

    <header class="holder">
      <h1 class="holder-name">YOUR NAME</h1>
      <p class="holder-title">Designation</p>
    </header>

    <div class="company">
      <span class="company-mark"></span>
      <span class="company-name">VoltaLine Inc.</span>
    </div>

    <p class="contact-text contact-phones">+ 000 - 1234 - 5678<br>+ 000 - 9876 - 5432</p>
    <p class="contact-text contact-web">name@companyname.com<br>www.website.com</p>
    <p class="contact-text contact-address">123 ABC Road,<br>XYZ 54321</p>
  </article>
</main>
</body>
</html>
```